I want 30 themed music album covers designing, from airoplanes, to cars, to animals,

All I need is text on a copywrite free picture, for example

Sound Clips & Effects. (top of album)

SFX Cars
Volume 1(bottom of album)

I need thirty thumbnails doing please.
Updates

Jungle, trains, industry,tools,household,storm,horror, sci-fi, farm, recreation, emergency,quotes, electronics,people, comic, office, cartoon, nautical, cars, nature, bells, musicals, battle, varied, background, water, aircraft, animals, medical, vehicle,trucks,

We need a themed photo/picture

They all then need to be thumb nail example;

SOUND EFFECTS 
       JUNGLE

SFX SOUND BITES

I need this asap, you will get to use our reputation www.brasslanternaudio.com 

I'm about to make a choice, any last minute offers, please submit 1 example and price for all asked for!

I have now increased budgets!!!!! 

Target Market(s)

Designers,

Requirements
Must have
• ASAP
Nice to have
• Pictures to represent theme really well
Should not have
• Blurred, unproffesional

```html
<!DOCTYPE html>
<html lang="en">
<head>
<meta charset="utf-8">
<title>Sound Clips &amp; Effects – SFX Cars Volume 1</title>
<link rel="stylesheet" href="https://fonts.googleapis.com/css2?family=Bangers&display=swap">
<style>
  :root {
    --page-bg: #ffffff;
    --cover-deep: #050d1e;
    --cover-navy: #0a2550;
    --cover-blue: #14579d;
    --cover-glow: #3f9fe6;
    --grid-line: rgba(90, 170, 240, 0.16);
    --title-fill: #ffffff;
    --title-stroke: #1a4d9e;
    --label-fill: #ffffff;
    --art-light: #f4f7fb;
    --art-mid: #b9c4d2;
    --art-dark: #1a1e27;
  }
  * { margin: 0; padding: 0; box-sizing: border-box; }
  html, body {
    width: 1200px;
    height: 960px;
    overflow: hidden;
    background: var(--page-bg);
  }
  .album-cover {
    position: absolute;
    left: 182px;
    top: 68px;
    width: 822px;
    height: 818px;
    overflow: hidden;
    background: var(--cover-deep);
    box-shadow: 8px 10px 8px rgba(0, 0, 0, 0.45);
  }
  .cover-backdrop {
    position: absolute;
    inset: 0;
    background:
      linear-gradient(118deg, transparent 47%, rgba(63,159,230,0.55) 50%, transparent 53%),
      linear-gradient(62deg, transparent 58%, rgba(63,159,230,0.40) 61%, transparent 64%),
      linear-gradient(135deg, transparent 30%, rgba(63,159,230,0.30) 34%, transparent 38%),
      linear-gradient(75deg, transparent 20%, rgba(63,159,230,0.25) 23%, transparent 26%),
      radial-gradient(ellipse 35% 45% at 12% 30%, rgba(63,159,230,0.35), transparent 70%),
      radial-gradient(ellipse 40% 55% at 85% 50%, rgba(63,159,230,0.30), transparent 70%),
      radial-gradient(ellipse 45% 35% at 55% 80%, rgba(20,87,157,0.6), transparent 70%),
      linear-gradient(160deg, var(--cover-deep) 0%, var(--cover-navy) 30%, var(--cover-blue) 55%, var(--cover-navy) 80%, var(--cover-deep) 100%);
  }
  .cover-grid {
    position: absolute;
    left: 0;
    top: 500px;
    width: 520px;
    height: 260px;
    background:
      repeating-linear-gradient(0deg, var(--grid-line) 0 1px, transparent 1px 14px),
      repeating-linear-gradient(90deg, var(--grid-line) 0 1px, transparent 1px 14px);
    -webkit-mask-image: radial-gradient(ellipse at 50% 40%, #000 30%, transparent 75%);
    mask-image: radial-gradient(ellipse at 50% 40%, #000 30%, transparent 75%);
  }
  .cover-title {
    position: absolute;
    top: 48px;
    left: 56px;
    width: 720px;
    text-align: center;
    font-family: "Bangers", sans-serif;
    font-weight: 400;
    font-size: 82px;
    line-height: 1;
    letter-spacing: 0;
    color: var(--title-fill);
    -webkit-text-stroke: 6px var(--title-stroke);
    paint-order: stroke fill;
    text-shadow: 3px 4px 0 rgba(255,255,255,0.9), 5px 6px 2px rgba(0,0,0,0.4);
  }
  .cover-artwork {
    position: absolute;
    left: 82px;
    top: 308px;
    width: 656px;
    height: 268px;
    border-radius: 30px;
    background:
      radial-gradient(ellipse 70% 60% at 60% 45%, var(--art-light) 0%, var(--art-mid) 55%, var(--art-dark) 100%);
    opacity: 0.9;
  }
  .cover-label {
    position: absolute;
    left: 22px;
    top: 748px;
    font-family: "Bangers", sans-serif;
    font-weight: 400;
    font-size: 64px;
    line-height: 1;
    letter-spacing: 0;
    color: var(--label-fill);
    text-shadow: 2px 3px 2px rgba(0,0,0,0.5);
  }
</style>
</head>
<body>
  <main class="album-cover">
    <div class="cover-backdrop" role="img" aria-label="Dark blue abstract background with diagonal streaks of light"></div>
    <div class="cover-grid"></div>
    <h1 class="cover-title">Sound Clips &amp; Effects</h1>
    <div class="cover-artwork" role="img" aria-label="Black and white illustration of a futuristic sports car"></div>
    <p class="cover-label">SFX Cars - Volume 1</p>
  </main>
</body>
</html>
```